Personal development products that change your life

This is a direct selling business that sells personal development courses, but also sells the business as well if desired. This is not MLM, and there is no handling of the product required, nor hassling friends or family. We are looking for business minded people wanting to work their own hours and achieve a desirable income from this. A success image or happy image on a flyer would be great. I'd like the website address to be displayed as well thanks. www.gainpath-hub.com.au

Target Market(s)

Business-minded individuals searching for more finances. Self motivated, driven, interested in self development.

Industry/Entity Type

Business

Font styles to use
Sans Serif

Requirements
Must have
• Are you looking for
• - a franchise or business?
• - a change of career?
• - a back up income?
• Not MLM
• No product handling or shipping
• No hard sales required
• website: www.gainpath-hub.com.au
Nice to have
• A picture or background of excited person jumping in the air, or some similar.
• Worded to enrol people interested in achieving more financial headway, or flexible hours, or travel and do this business from anywhere in the world.
• Only need access to a phone, internet connection and a desire to succeed.

```html
<!DOCTYPE html>
<html lang="en">
<head>
<meta charset="utf-8">
<title>Personal Development Courses – Flyer</title>
<link rel="stylesheet" href="https://fonts.googleapis.com/css2?family=Roboto+Slab:wght@700;800&family=Teko:wght@300;400&family=Oswald:wght@400;500&family=Lato:ital,wght@0,400;0,700;0,900;1,400;1,700&display=swap">
<style>
  :root {
    --page-bg: #e6e8eb;
    --teal: #2f8ea8;
    --teal-bright: #3aa7c8;
    --teal-text: #3489a9;
    --navy: #1b2a57;
    --ink: #1e2f5c;
    --paper: #ffffff;
    --title-grey: #d9dadc;
  }
  * { margin: 0; padding: 0; box-sizing: border-box; }
  html, body { width: 904px; height: 1200px; overflow: hidden; background: var(--page-bg); }
  .flyer {
    position: absolute; left: 29px; top: 0;
    width: 846px; height: 1200px; overflow: hidden;
    background: var(--paper);
    font-family: "Lato", sans-serif;
  }
  .flyer-shapes { position: absolute; inset: 0; }

  .title {
    position: absolute; left: 19px; top: 18px;
    font-family: "Roboto Slab", serif; font-weight: 800;
    font-size: 46px; line-height: 66px; letter-spacing: 1px;
    color: var(--title-grey);
    text-shadow: 2px 2px 0 #6b6f78, 3px 4px 5px rgba(0,0,0,.45);
  }

  .offer-box { position: absolute; left: 545px; top: 402px; width: 250px; color: #fff; }
  .offer-box .per-sale {
    font-family: "Oswald", sans-serif; font-size: 22px; text-align: center; margin-bottom: 8px;
  }
  .offer-box .doing {
    font-weight: 700; font-size: 23px; line-height: 33px; text-align: center; margin-bottom: 12px;
  }
  .offer-box ul { list-style: none; font-weight: 700; font-size: 17.5px; line-height: 22px; }
  .offer-box li { position: relative; padding-left: 18px; }
  .offer-box li::before {
    content: ""; position: absolute; left: 2px; top: 6px;
    width: 10px; height: 10px; border-radius: 50%; background: #fff;
  }

  .headline {
    position: absolute; left: 23px; top: 522px;
    font-family: "Teko", sans-serif; font-weight: 400;
    font-size: 70px; line-height: 1; color: var(--teal-text); white-space: nowrap;
  }

  .looking { position: absolute; left: 22px; top: 650px; color: var(--ink); }
  .looking h2 {
    font-family: "Teko", sans-serif; font-weight: 400; font-size: 38px; line-height: 1;
    margin-bottom: 6px;
  }
  .looking ul { list-style: none; font-style: italic; font-size: 19px; line-height: 36px; }
  .looking li { display: flex; align-items: center; gap: 22px; }
  .looking li svg { width: 12px; height: 14px; flex: none; }

  .badge { position: absolute; left: 309px; top: 619px; width: 200px; height: 200px; }
  .badge-text {
    position: absolute; inset: 0; display: flex; flex-direction: column;
    align-items: center; justify-content: center;
    transform: rotate(20deg);
    font-family: "Roboto Slab", serif; font-weight: 700; color: #fff;
    font-size: 24px; line-height: 30px; text-align: center;
  }

  .balance { position: absolute; left: 25px; top: 826px; }
  .balance .lead { font-weight: 700; font-size: 25px; line-height: 32px; color: var(--teal-text); }
  .balance .tail { font-size: 25px; line-height: 32px; color: var(--ink); }

  .ongoing { position: absolute; left: 25px; top: 912px; color: var(--ink); }
  .ongoing .lead { font-weight: 900; font-size: 23px; line-height: 31px; }
  .ongoing .tail { font-weight: 700; font-style: italic; font-size: 25px; line-height: 34px; }

  .footer-note {
    position: absolute; left: 22px; top: 1103px;
    font-style: italic; font-weight: 700; color: #fff; font-size: 16.5px; line-height: 24px;
  }
  .website {
    position: absolute; left: 22px; top: 1160px;
    font-weight: 700; font-size: 23px; color: var(--teal-bright);
  }
</style>
</head>
<body>
<main class="flyer">
  <svg class="flyer-shapes" width="846" height="1200" viewBox="0 0 846 1200">
    <defs>
      <linearGradient id="sky-grad" x1="0" y1="0" x2="0" y2="1">
        <stop offset="0" stop-color="#5a84c2"/>
        <stop offset="1" stop-color="#6f97cf"/>
      </linearGradient>
      <linearGradient id="faint-grad" x1="0" y1="0" x2="1" y2="1">
        <stop offset="0" stop-color="#f4f5f7"/>
        <stop offset="0.5" stop-color="#e3e6ea"/>
        <stop offset="1" stop-color="#eef0f3"/>
      </linearGradient>
      <linearGradient id="para-grad" x1="0" y1="0" x2="0" y2="1">
        <stop offset="0" stop-color="#4c8fe0"/>
        <stop offset="1" stop-color="#7eb2ec"/>
      </linearGradient>
      <linearGradient id="ski-grad" x1="0" y1="0" x2="0" y2="1">
        <stop offset="0" stop-color="#3d6fb8"/>
        <stop offset="0.6" stop-color="#b8c9df"/>
        <stop offset="1" stop-color="#8a9cb6"/>
      </linearGradient>
      <linearGradient id="navy-grad" x1="0" y1="0" x2="1" y2="0">
        <stop offset="0" stop-color="#1c3266"/>
        <stop offset="1" stop-color="#14204a"/>
      </linearGradient>
    </defs>

    <rect x="0" y="470" width="540" height="640" fill="url(#faint-grad)"
          role="img" aria-label="Faint background photo of a person swinging on a rope above water"/>

    <polygon points="0,0 846,0 846,330 286,480 0,410" fill="url(#sky-grad)"
             role="img" aria-label="Photo of a young man leaping joyfully between rocks against a blue sky"/>

    <polygon points="0,410 286,480 560,407 560,440 286,520 0,452" fill="var(--teal-bright)"/>
    <polygon points="0,452 286,520 560,440 560,450 286,532 0,462" fill="var(--navy)"/>
    <polygon points="0,462 286,532 560,450 560,456 286,540 0,468" fill="#ffffff"/>
    <polygon points="620,392 846,330 846,344 620,406" fill="var(--navy)"/>

    <polygon points="529,396 804,312 804,624 529,684" fill="var(--teal)"/>
    <polygon points="529,694 804,634 804,652 529,716" fill="var(--navy)"/>
    <polygon points="610,660 804,618 804,628 610,670" fill="var(--teal-bright)"/>

    <rect x="536" y="726" width="270" height="166" fill="url(#para-grad)"
          role="img" aria-label="Photo of a paraglider pilot in a red jacket flying in a blue sky"/>
    <rect x="536" y="726" width="270" height="166" fill="none" stroke="#ffffff" stroke-width="2"/>

    <polygon points="0,1100 252,1024 846,1150 846,1200 0,1200" fill="url(#navy-grad)"/>
    <polygon points="0,1084 252,1010 290,1016 0,1098" fill="var(--teal-bright)"/>
    <polygon points="536,1090 846,1150 846,1172 536,1110" fill="var(--teal-bright)"/>

    <polygon points="536,908 806,908 806,1192 536,1102" fill="url(#ski-grad)"
             role="img" aria-label="Photo of a skier in a red jacket jumping mid-air over snowy mountains"/>
    <polygon points="536,908 806,908 806,1192 536,1102" fill="none" stroke="#ffffff" stroke-width="2"/>

    <g transform="translate(409 719)">
      <polygon fill="var(--teal)" stroke="#ffffff" stroke-width="4"
        points="96,0 80.4,16 88.7,36.8 68.1,45.6 67.9,67.9 45.6,68.1 36.8,88.7 16,80.4 0,96 -16,80.4 -36.8,88.7 -45.6,68.1 -67.9,67.9 -68.1,45.6 -88.7,36.8 -80.4,16 -96,0 -80.4,-16 -88.7,-36.8 -68.1,-45.6 -67.9,-67.9 -45.6,-68.1 -36.8,-88.7 -16,-80.4 0,-96 16,-80.4 36.8,-88.7 45.6,-68.1 67.9,-67.9 68.1,-45.6 88.7,-36.8 80.4,-16"/>
    </g>
  </svg>

  <h1 class="title">PERSONAL<br>DEVELOPMENT<br>COURSES</h1>

  <section class="offer-box">
    <p class="per-sale">Earn up to $8000 per sale!</p>
    <p class="doing">Turn this into DOING<br>what YOU love!</p>
    <ul>
      <li>Not MLM</li>
      <li>No product handling<br>or shipping</li>
      <li>No hard sales required</li>
    </ul>
  </section>

  <p class="headline">Earn as little as $1800</p>

  <section class="looking">
    <h2>ARE YOU LOOKING FOR</h2>
    <ul>
      <li><svg viewBox="0 0 12 14"><polyline points="2,1 9,7 2,13" fill="none" stroke="var(--navy)" stroke-width="3"/></svg>A franchise or business?</li>
      <li><svg viewBox="0 0 12 14"><polyline points="2,1 9,7 2,13" fill="none" stroke="var(--navy)" stroke-width="3"/></svg>A change of career?</li>
      <li><svg viewBox="0 0 12 14"><polyline points="2,1 9,7 2,13" fill="none" stroke="var(--navy)" stroke-width="3"/></svg>A back up income?</li>
    </ul>
  </section>

  <div class="badge"><div class="badge-text"><span>YOU</span><span>CAN DO</span><span>THIS TOO!</span></div></div>

  <section class="balance">
    <p class="lead">START THE WORK / LIFE BALANCE</p>
    <p class="tail">you've always wanted.</p>
  </section>

  <section class="ongoing">
    <p class="lead">ONGOING PERSONAL<br>DEVELOPMENT OPPORTUNITIES</p>
    <p class="tail">for successful applicants</p>
  </section>

  <p class="footer-note">All you need is a laptop, a phone, a strong desire to succeed,<br>and dedicate 15-20 hours per week.</p>
  <p class="website">www.gainpath-hub.com.au</p>
</main>
</body>
</html>
```